Business Card for Ferncliff Massage

I need a business card for my massage therapy & cannabis oil practice. I already have a logo,the "massage" got edited out of this file. I will send the original soon. I need these elements to be on the card:
web: FerncliffMassage.example
ph: 417/283-9061
email: Mirela.Dawkant@mailbox.example
Other slogans, statements to consider:
Science Geek, Massage Therapist, Neuromuscular Therapy, Cannabis Spa Treatments, Raindrop Therapy, Essential Oils
Target Market(s)
women between 20 & 65, people with enough $ to afford regular massage, people who recently had a motor vehicle accident, Halvora HMP insured
Industry/Entity Type
Massage Therapy
Contact Information for Business Card
I would like to see my bear logo featured; contact details, greens & blues preferred colors.

```html
<!DOCTYPE html>
<html lang="en">
<head>
<meta charset="utf-8">
<title>Ferncliff Massage — Business Card</title>
<link rel="stylesheet" href="https://fonts.googleapis.com/css2?family=Encode+Sans+Condensed:wght@300;400;600&display=swap">
<style>
  :root {
    --page: #ecebe8;
    --white: #ffffff;
    --green: #2f8a3c;
    --green-dark: #267432;
    --taupe: #8b7e75;
    --taupe-light: #a4968c;
    --taupe-dark: #74675f;
    --ink-soft: #f4f1ee;
    --shadow: rgba(0, 0, 0, 0.18);
  }
  * { box-sizing: border-box; margin: 0; padding: 0; }
  html, body {
    width: 1200px; height: 950px; overflow: hidden;
    background: var(--page);
    font-family: "Encode Sans Condensed", "Arial Narrow", sans-serif;
  }
  .card {
    position: absolute; left: 250px;
    width: 700px; height: 400px;
    border-radius: 24px; overflow: hidden;
    box-shadow: 0 10px 26px var(--shadow);
  }
  .card--front { top: 55px; background: var(--white); }
  .card--back {
    top: 495px;
    background: radial-gradient(ellipse at 38% 35%, var(--taupe-light) 0%, var(--taupe) 55%, var(--taupe-dark) 100%);
    color: var(--white);
  }
  .front-shapes { position: absolute; inset: 0; }

  .brand {
    position: absolute; left: 190px; top: 88px;
    display: flex; align-items: center; gap: 18px;
  }
  .brand__dot { width: 46px; height: 46px; border-radius: 50%; background: var(--taupe); }
  .brand__name {
    font-weight: 300; font-size: 74px; line-height: 1;
    color: var(--green); letter-spacing: 1px;
  }

  .person { position: absolute; left: 38px; top: 262px; color: var(--white); }
  .person__name { font-weight: 600; font-size: 22px; letter-spacing: 1px; text-transform: uppercase; }
  .person__role { font-weight: 300; font-size: 16px; margin-top: 2px; }
  .contact { list-style: none; margin-top: 12px; font-weight: 300; font-size: 15px; }
  .contact li { display: flex; align-items: center; gap: 9px; height: 22px; }
  .contact svg { width: 14px; height: 14px; flex: none; }

  .social { position: absolute; right: 38px; top: 228px; display: flex; gap: 7px; }
  .social span { width: 20px; height: 20px; border-radius: 50%; background: var(--white); }

  .back-brand {
    position: absolute; right: 60px; top: 70px; text-align: right;
  }
  .back-brand__name { font-weight: 300; font-size: 70px; line-height: 1; letter-spacing: 1px; }
  .back-brand__web { font-weight: 300; font-size: 17px; margin-top: 4px; color: var(--ink-soft); }
  .services { position: absolute; right: 60px; top: 200px; text-align: right; }
  .services__title { font-weight: 600; font-size: 18px; letter-spacing: 1px; text-transform: uppercase; margin-bottom: 4px; }
  .services__list { list-style: none; font-weight: 300; font-style: normal; font-size: 17px; line-height: 23px; }
  .services__list li::after { content: " •"; }
</style>
</head>
<body>

<section class="card card--front" aria-label="Business card front">
  <svg class="front-shapes" width="700" height="400" viewBox="0 0 700 400" aria-hidden="true">
    <path d="M330 190 Q345 178 365 178 L700 178 L700 400 L330 400 Z" fill="var(--taupe)"/>
    <path d="M0 228 L300 228 Q318 228 330 212 Q344 194 365 194 L700 194 L700 400 L0 400 Z" fill="var(--green)"/>
    <line x1="350" y1="250" x2="640" y2="250" stroke="var(--white)" stroke-width="1.5"/>
  </svg>

  <div class="brand">
    <span class="brand__dot"></span>
    <span class="brand__name">Ferncliff</span>
  </div>

  <div class="social" aria-label="Social links">
    <span></span><span></span>
  </div>

  <div class="person">
    <p class="person__name">Arlo Pennick</p>
    <p class="person__role">CEO/Founder</p>
    <ul class="contact">
      <li>
        <svg viewBox="0 0 16 16" aria-hidden="true"><path d="M4 1.5 6.5 4 5 6c1 2 3 4 5 5l2-1.5 2.5 2.5-2 2.5C7 14 2 9 1.5 3.5Z" fill="var(--white)"/></svg>
        417/283-9061
      </li>
      <li>
        <svg viewBox="0 0 16 16" aria-hidden="true"><rect x="1" y="3" width="14" height="10" rx="1.5" fill="var(--white)"/><path d="M1.5 4 8 9l6.5-5" fill="none" stroke="var(--green)" stroke-width="1.4"/></svg>
        Mirela.Dawkant@mailbox.example
      </li>
      <li>
        <svg viewBox="0 0 16 16" aria-hidden="true"><circle cx="8" cy="8" r="7" fill="var(--white)"/><path d="M1 8h14M8 1c3 3 3 11 0 14M8 1c-3 3-3 11 0 14" fill="none" stroke="var(--green)" stroke-width="1.1"/></svg>
        FerncliffMassage.example
      </li>
    </ul>
  </div>
</section>

<section class="card card--back" aria-label="Business card back">
  <div class="back-brand">
    <p class="back-brand__name">Ferncliff</p>
    <p class="back-brand__web">www.FerncliffMassage.example</p>
  </div>
  <div class="services">
    <p class="services__title">Services</p>
    <ul class="services__list">
      <li>Science Geek</li>
      <li>Massage Therapist</li>
      <li>Neuromuscular Therapy</li>
      <li>Cannabis Spa Treatments</li>
      <li>Raindrop Therapy</li>
      <li>Essential Oils</li>
    </ul>
  </div>
</section>

</body>
</html>
```